Business cards for investing fund

I need processional luxury classical business cards for CEO of the investing company. I need it to be elegant. I need it to look expensive. It will be printed o fine paper with UV. I prefer light and minimalistic design. Logo of my company must be included at least on front page.

Target Market(s)

40+ investors

Industry/Entity Type

Finance And Accounting

Contact Information for Business Card

FRONT PAGE:

Wiktor Osmalek
President & CEO

e: vik@brlcap.example
w: www.brlcap.example
p: +44 20 7395 2847
m: +44 75 2918 3406

Brass Lark Venture Capital, LLC
17 W Pinecrest Ave., Sheridan, WY 82801
Filling number: 2019-000542319

BACK PAGE (with or without logo):

PROUD GROUP MEMBERS:

UK: Marrow Bay Associates Ltd. | 42 Elmsworth Row, 1st fl. | W1T-4QR London
PL: Marrow Bay Trust S.A. | ul. Lipowa Polna 14, 4p. | 00-871 Warszawa
US: Crestfall Advisors, LLC | 213 Orchard Lane, Suite 409, NYC | 10017 New York

Font styles to use
Serif
Sans Serif
Decorative

Colors
0355a3
ec1f27

Requirements
Must have
• My own logo (attached)

```html
<!DOCTYPE html>
<html lang="en">
<head>
<meta charset="utf-8">
<title>Brass Lark Venture Capital — Business Card</title>
<link rel="stylesheet" href="https://fonts.googleapis.com/css2?family=Open+Sans:ital,wght@0,400;0,700;1,700&family=Playfair+Display:wght@700&display=swap">
<style>
  :root {
    --brand-blue: #0b58a6;
    --card-white: #ffffff;
    --ink-grey: #3c3c3c;
    --band-dark: #4a4a4a;
    --rule-grey: #c9c9c9;
    --backdrop: #e6e7e9;
    --serif: "Playfair Display", Georgia, serif;
    --sans: "Open Sans", Arial, sans-serif;
  }
  * { box-sizing: border-box; margin: 0; padding: 0; }
  html, body { width: 1200px; height: 782px; overflow: hidden; }
  body {
    background: var(--backdrop);
    font-family: var(--sans);
    position: relative;
  }
  .card {
    position: absolute;
    top: 236px;
    width: 540px;
    height: 309px;
    box-shadow: 0 6px 18px rgba(0,0,0,.18);
    overflow: hidden;
  }
  /* Front */
  .card-front { left: 40px; background: var(--card-white); }
  .brand-name {
    position: absolute;
    left: 34px; top: 104px;
    width: 200px;
    font-family: var(--serif);
    font-weight: 700;
    font-size: 30px;
    line-height: 1.05;
    color: var(--brand-blue);
  }
  .divider {
    position: absolute;
    left: 252px; top: 58px;
    width: 1px; height: 178px;
    background: linear-gradient(to bottom, transparent, var(--rule-grey) 30%, var(--rule-grey) 70%, transparent);
  }
  .contact {
    position: absolute;
    left: 274px; top: 56px;
    color: var(--ink-grey);
  }
  .holder-name {
    font-family: var(--serif);
    font-weight: 700;
    font-size: 22px;
    letter-spacing: .5px;
    color: var(--brand-blue);
    text-transform: uppercase;
    line-height: 1.1;
  }
  .holder-title { font-size: 14px; margin-bottom: 6px; }
  .contact-list { list-style: none; font-size: 14px; line-height: 21px; }
  .contact-list li { display: flex; align-items: center; gap: 8px; }
  .contact-list svg { width: 12px; height: 12px; flex: none; }
  .address { font-size: 14px; line-height: 20px; margin-top: 2px; }
  .bottom-band { position: absolute; left: 0; bottom: 0; width: 540px; height: 44px; }
  .filing {
    position: absolute;
    right: 22px; bottom: 9px;
    color: #fff;
    font-size: 15px;
    letter-spacing: .3px;
  }
  .filing strong { font-weight: 700; font-style: italic; }
  /* Back */
  .card-back {
    left: 620px;
    background: var(--brand-blue);
    color: #fff;
    text-align: center;
    display: flex; flex-direction: column; justify-content: center;
    font-size: 13.5px;
    line-height: 19px;
    padding-left: 40px;
  }
  .members-heading { font-weight: 700; font-size: 12.5px; letter-spacing: .3px; margin-bottom: 8px; }
  .member { margin-bottom: 8px; }
  .member b { font-weight: 700; }
</style>
</head>
<body>
  <section class="card card-front">
    <div class="brand-name">Brass Lark Venture Capital, LLC</div>
    <div class="divider"></div>
    <div class="contact">
      <h1 class="holder-name">Wiktor Osmalek</h1>
      <p class="holder-title">President &amp; CEO</p>
      <ul class="contact-list">
        <li><svg viewBox="0 0 12 12" aria-hidden="true"><rect width="12" height="12" rx="2" fill="var(--brand-blue)"/><path d="M3 3.2c.5 2.6 2.4 4.8 5.8 5.8l.7-1.3-1.6-.8-.7.7c-1-.5-1.8-1.3-2.3-2.3l.7-.7-.8-1.6z" fill="#fff"/></svg>+44 20 7395 2847</li>
        <li><svg viewBox="0 0 12 12" aria-hidden="true"><rect width="12" height="12" rx="2" fill="var(--brand-blue)"/><rect x="4" y="2.2" width="4" height="7.6" rx=".8" fill="#fff"/></svg>+44 75 2918 3406</li>
        <li><svg viewBox="0 0 12 12" aria-hidden="true"><rect width="12" height="12" rx="2" fill="var(--brand-blue)"/><rect x="2.5" y="3.5" width="7" height="5" fill="#fff"/><path d="M2.5 3.5 6 6.5l3.5-3" stroke="var(--brand-blue)" stroke-width=".8" fill="none"/></svg>vik@brlcap.example</li>
        <li><svg viewBox="0 0 12 12" aria-hidden="true"><rect width="12" height="12" rx="2" fill="var(--brand-blue)"/><circle cx="6" cy="6" r="3.4" stroke="#fff" stroke-width=".9" fill="none"/><path d="M2.6 6h6.8M6 2.6v6.8" stroke="#fff" stroke-width=".7"/></svg>www.brlcap.example</li>
      </ul>
      <p class="address">17 W Pinecrest Ave.<br>Sheridan, WY 82801</p>
    </div>
    <svg class="bottom-band" viewBox="0 0 540 44" preserveAspectRatio="none" aria-hidden="true">
      <polygon points="0,20 262,20 248,44 0,44" fill="var(--brand-blue)"/>
      <polygon points="268,8 540,8 540,44 248,44" fill="var(--band-dark)"/>
    </svg>
    <p class="filing">Filling number: <strong>2019-000542319</strong></p>
  </section>

  <section class="card card-back">
    <p class="members-heading">PROUD GROUP MEMBERS</p>
    <p class="member"><b>UK:</b> Marrow Bay Associates Ltd.<br>42 Elmsworth Row, 1st fl. | W1T-4QR London</p>
    <p class="member"><b>PL:</b> Marrow Bay Trust S.A.<br>ul. Lipowa Polna 14, 4p. | 00-871 Warszawa</p>
    <p class="member"><b>US:</b> Crestfall Advisors, LLC<br>213 Orchard Lane, Suite 409, NYC | 10017 New York</p>
  </section>
</body>
</html>
```